Need business cards for our e-assessment business

We need professional looking business cards for our e-assessment business based in Europe. Our company is called Velnor.

You can just use sample name and addresses.

The colours we use are:

#70abe4 (blue)
#FF6600 (orange)

The back side should say: E-assessment made easy

This is the print-shop we are using. Please look at the link for info about formats: http://nl.printqet.com/help/faq/using-my-own-artwork.html

Target Market(s)

Target market is education and large corporations

Industry/Entity Type

Business

```html
<!DOCTYPE html>
<html lang="en">
<head>
<meta charset="utf-8">
<title>Velnor business cards</title>
<link rel="stylesheet" href="https://fonts.googleapis.com/css2?family=Open+Sans:wght@400;600;700&family=Over+the+Rainbow&display=swap">
<style>
  :root {
    --brand-blue: #70abe4;
    --brand-orange: #ff6600;
    --soft-peach: #fde3d2;
    --ink: #3a3a3a;
    --text: #2b2b2b;
    --card: #ffffff;
    --backdrop: #e8e5e1;
  }
  * { margin: 0; padding: 0; box-sizing: border-box; }
  html, body { width: 1200px; height: 1000px; overflow: hidden; }
  body {
    background: var(--backdrop);
    font-family: "Open Sans", Arial, sans-serif;
    color: var(--text);
    position: relative;
  }
  .card {
    position: absolute;
    left: 310px;
    width: 580px;
    height: 350px;
    background: var(--card);
    overflow: hidden;
    box-shadow: 0 6px 18px rgba(0,0,0,0.18);
  }
  .card--front { top: 90px; }
  .card--back { top: 530px; }

  .accent-circle {
    position: absolute;
    border-radius: 50%;
    background: var(--soft-peach);
  }
  .card--front .accent-circle { width: 200px; height: 200px; left: 345px; top: 100px; }
  .card--back .accent-circle { width: 205px; height: 205px; left: 357px; top: 60px; }

  .brand {
    position: absolute;
    left: 34px;
    top: 30px;
    display: flex;
    align-items: center;
    gap: 28px;
  }
  .brand__mark {
    width: 92px;
    height: 92px;
    border-radius: 50%;
    background: var(--brand-orange);
  }
  .brand__name {
    font-size: 68px;
    font-weight: 400;
    color: var(--ink);
    letter-spacing: 0.5px;
    line-height: 1;
    margin-top: 18px;
  }

  .contact {
    position: absolute;
    left: 50px;
    top: 168px;
  }
  .contact__name { font-size: 22px; font-weight: 400; line-height: 1.1; }
  .contact__line { font-size: 13px; font-weight: 600; line-height: 1.3; }
  .contact__line--email { margin-top: 18px; }

  .stripe-area {
    position: absolute;
    left: 0;
    bottom: 10px;
    width: 580px;
    height: 56px;
    background: linear-gradient(90deg,
      rgba(255,102,0,0) 0%,
      rgba(255,102,0,0.35) 30%,
      rgba(112,171,228,0.55) 100%);
  }

  .top-band {
    position: absolute;
    left: 0;
    top: 0;
    width: 580px;
    height: 44px;
    background: var(--brand-blue);
  }

  .tagline {
    position: absolute;
    left: 18px;
    top: 146px;
    font-family: "Over the Rainbow", cursive;
    font-size: 26px;
    line-height: 1.2;
    color: #1e1e1e;
    white-space: nowrap;
  }
</style>
</head>
<body>

  <section class="card card--front" aria-label="Business card front">
    <div class="accent-circle"></div>
    <div class="brand">
      <span class="brand__mark"></span>
      <span class="brand__name">velnor</span>
    </div>
    <div class="contact">
      <p class="contact__name">Bussiness Name</p>
      <p class="contact__line">Contact no.</p>
      <p class="contact__line contact__line--email">Email adress:</p>
    </div>
    <div class="stripe-area" role="img" aria-label="Decorative orange and blue stripe motif"></div>
  </section>

  <section class="card card--back" aria-label="Business card back">
    <div class="top-band"></div>
    <div class="accent-circle"></div>
    <p class="tagline">E-assessment made easy</p>
    <div class="stripe-area" role="img" aria-label="Decorative orange and blue stripe motif"></div>
  </section>

</body>
</html>
```